Album Cover Art for "Harmonux: The Loop Reel"

This will be an album of 5 beats/instrumentals, professionally called a "Beat Tape." The type of music that will be on here all have a melodic, R&Bish, souful vibe with dynamic drum sounds.

More detail that could help;
--My theme as a music producer is a spaced out and out of this world or galaxy sound.
-And for this cover, think of Harmonux like a school subject and have that out of this world aspect.
-The first name of my producer name is R4ndal and it real life, Kelvin is the temperature of the universe. With me using it as my name, I'm saying my music is that HOT.
-Be as creative as you can be. You can follow your own ideas as well.

I would like the following texts to be on the front cover;

Harmonux: The Loop Reel
By: R4NDAL V▲PR

These are the names of the tracks for the back cover;
1.Stay Golden(Prod. R4ndal Vapr)
2.VIBE(Prod. R4ndal Vapr)
3.U Still Here(Prod. R4ndal Vapr)
4. Late Night Bae(Prod. R4ndal Vapr)
5.Head Tr*P(Prod. R4ndal Vapr)

Also,somewhere on back put social media icons for IG,FB,YT,TW and have @r4ndalvapr

My logo is attached as well.

Thanks!

```html
<!DOCTYPE html>
<html lang="en">
<head>
<meta charset="utf-8">
<title>Harmonux: The Loop Reel</title>
<link href="https://fonts.googleapis.com/css2?family=Teko:wght@500;600&family=Cinzel:wght@400&family=Montserrat:wght@600;700&display=swap" rel="stylesheet">
<style>
  :root {
    --page: #ffffff;
    --space-deep: #2c2f5a;
    --space-mid: #1f6a78;
    --space-teal: #2fa59a;
    --space-glow: #5fd0b4;
    --ink-light: #ffffff;
    --ink-soft: #e6f3f1;
    --disc-hub: #3a3d44;
    --disc-ring: #9aa3a8;
  }
  html, body {
    margin: 0;
    padding: 0;
    width: 1200px;
    height: 3124px;
    overflow: hidden;
    background: var(--page);
  }
  .canvas {
    position: relative;
    width: 1200px;
    height: 3124px;
    background: var(--page);
  }
  .panel {
    position: absolute;
    overflow: hidden;
    color: var(--ink-light);
  }
  .nebula {
    position: absolute;
    inset: 0;
    background:
      radial-gradient(ellipse 45% 30% at 58% 45%, rgba(95,208,180,0.55), transparent 70%),
      radial-gradient(ellipse 60% 40% at 40% 60%, rgba(47,165,154,0.5), transparent 75%),
      linear-gradient(165deg, var(--space-mid) 0%, var(--space-teal) 38%, var(--space-mid) 62%, var(--space-deep) 100%);
  }
  .nebula--back {
    background:
      radial-gradient(ellipse 50% 30% at 50% 55%, rgba(95,208,180,0.5), transparent 70%),
      radial-gradient(ellipse 55% 35% at 35% 80%, rgba(95,208,180,0.45), transparent 75%),
      linear-gradient(180deg, var(--space-deep) 0%, var(--space-mid) 35%, var(--space-teal) 75%, var(--space-mid) 100%);
  }
  .centered {
    position: absolute;
    left: 50%;
    transform: translateX(-50%);
    text-align: center;
    white-space: nowrap;
  }
  .album-title {
    margin: 0;
    font-family: "Teko", sans-serif;
    font-weight: 600;
    font-size: 11.5em;
    line-height: 0.8;
    letter-spacing: 0.02em;
    text-shadow: 0 0 0.25em rgba(255,255,255,0.45);
  }
  .album-subtitle {
    font-family: "Teko", sans-serif;
    font-weight: 500;
    font-size: 3.4em;
    letter-spacing: 0.32em;
    line-height: 1;
  }
  .tape-list-heading {
    font-family: "Cinzel", serif;
    font-size: 3.2em;
    letter-spacing: 0.08em;
  }
  .track {
    font-family: "Montserrat", sans-serif;
    font-weight: 700;
    font-size: 2.35em;
  }
  .producer-mark {
    display: flex;
    flex-direction: column;
    align-items: center;
    gap: 0.4em;
  }
  .producer-mark__dot {
    width: 5em;
    height: 5em;
    border: 0.25em solid var(--ink-light);
    border-radius: 50%;
    box-sizing: border-box;
  }
  .producer-mark__name {
    font-family: "Montserrat", sans-serif;
    font-weight: 700;
    font-size: 1.5em;
    letter-spacing: 0.06em;
  }
  .producer-mark__tag {
    font-family: "Montserrat", sans-serif;
    font-weight: 700;
    font-size: 0.8em;
    letter-spacing: 0.2em;
    color: var(--ink-soft);
  }
  .producer-mark--corner {
    position: absolute;
    right: 4.5%;
    bottom: 3.5%;
  }
  .handle {
    font-family: "Montserrat", sans-serif;
    font-weight: 700;
    font-size: 1.8em;
  }
  .social-row {
    display: flex;
    gap: 0.7em;
  }
  .social-row__dot {
    width: 2em;
    height: 2em;
    border-radius: 50%;
    background: var(--ink-light);
  }

  /* panel placements */
  .front-cover   { left: 248px; top: 167px;  width: 678px; height: 678px; font-size: 6.78px; }
  .back-cover    { left: 248px; top: 952px;  width: 683px; height: 683px; font-size: 6.83px; }
  .front-cover--small { left: 355px; top: 1800px; width: 490px; height: 490px; font-size: 4.9px; }
  .back-cover--booklet { left: 143px; top: 2452px; width: 425px; height: 459px; font-size: 4.25px; }

  .disc {
    position: absolute;
    left: 653px;
    top: 2529px;
    width: 392px;
    height: 392px;
    border-radius: 50%;
    overflow: hidden;
    font-size: 3.92px;
    color: var(--ink-light);
  }
  .disc .nebula { border-radius: 50%; }
  .disc__hub {
    position: absolute;
    left: 50%;
    top: 50%;
    width: 34%;
    height: 34%;
    transform: translate(-50%, -50%);
    border-radius: 50%;
    background: var(--disc-hub);
    border: 0.9em solid var(--disc-ring);
    box-sizing: border-box;
  }
  .disc__hole {
    position: absolute;
    left: 50%;
    top: 50%;
    width: 10%;
    height: 10%;
    transform: translate(-50%, -50%);
    border-radius: 50%;
    background: var(--page);
  }
</style>
</head>
<body>
<main class="canvas">

  <section class="panel front-cover">
    <div class="nebula" role="img" aria-label="Teal and violet galaxy nebula with scattered stars"></div>
    <div class="centered" style="top:11%">
      <h1 class="album-title">HARMONUX</h1>
      <div class="album-subtitle">THE LOOP REEL</div>
    </div>
    <div class="producer-mark producer-mark--corner">
      <span class="producer-mark__dot"></span>
      <span class="producer-mark__name">R4NDAL V▲PR</span>
      <span class="producer-mark__tag">THE HARMONIC ERA</span>
    </div>
  </section>

  <section class="panel back-cover">
    <div class="nebula nebula--back" role="img" aria-label="Teal galaxy nebula glowing across a starry deep blue sky"></div>
    <div class="centered" style="top:11%">
      <h2 class="album-title">HARMONUX</h2>
      <div class="album-subtitle">THE LOOP REEL</div>
    </div>
    <div class="centered tape-list-heading" style="top:33%">TAPE LIST</div>
    <div class="centered track" style="top:42%">1. Stay Golden(Prod. R4ndal Vapr)</div>
    <div class="centered track" style="top:48%">2. VIBE(Prod. R4ndal Vapr)</div>
    <div class="centered track" style="top:54%">3. U Still Here(Prod. R4ndal Vapr)</div>
    <div class="centered track" style="top:60%">4. Late Night Bae(Prod. R4ndal Vapr)</div>
    <div class="centered track" style="top:66%">5. Head Tr*P(Prod. R4ndal Vapr)</div>
    <div class="centered producer-mark" style="top:76%">
      <span class="producer-mark__dot"></span>
      <span class="producer-mark__name">R4NDAL V▲PR</span>
    </div>
    <div class="centered handle" style="top:87%">@r4ndalvapr</div>
    <div class="centered social-row" style="top:91%" aria-hidden="true">
      <span class="social-row__dot"></span><span class="social-row__dot"></span><span class="social-row__dot"></span><span class="social-row__dot"></span>
    </div>
  </section>

  <section class="panel front-cover--small">
    <div class="nebula" role="img" aria-label="Teal and violet galaxy nebula with scattered stars"></div>
    <div class="centered" style="top:11%">
      <h2 class="album-title">HARMONUX</h2>
      <div class="album-subtitle">THE LOOP REEL</div>
    </div>
    <div class="producer-mark producer-mark--corner">
      <span class="producer-mark__dot"></span>
      <span class="producer-mark__name">R4NDAL V▲PR</span>
      <span class="producer-mark__tag">THE HARMONIC ERA</span>
    </div>
  </section>

  <section class="panel back-cover--booklet">
    <div class="nebula nebula--back" role="img" aria-label="Teal galaxy nebula glowing across a starry deep blue sky"></div>
    <div class="centered" style="top:10%">
      <h2 class="album-title">HARMONUX</h2>
      <div class="album-subtitle">THE LOOP REEL</div>
    </div>
    <div class="centered tape-list-heading" style="top:31%">TAPE LIST</div>
    <div class="centered track" style="top:40%">1. Stay Golden(Prod. R4ndal Vapr)</div>
    <div class="centered track" style="top:46%">2. VIBE(Prod. R4ndal Vapr)</div>
    <div class="centered track" style="top:52%">3. U Still Here(Prod. R4ndal Vapr)</div>
    <div class="centered track" style="top:58%">4. Late Night Bae(Prod. R4ndal Vapr)</div>
    <div class="centered track" style="top:64%">5. Head Tr*P(Prod. R4ndal Vapr)</div>
    <div class="centered producer-mark" style="top:73%">
      <span class="producer-mark__dot"></span>
      <span class="producer-mark__name">R4NDAL V▲PR</span>
    </div>
    <div class="centered handle" style="top:86%">@r4ndalvapr</div>
    <div class="centered social-row" style="top:91%" aria-hidden="true">
      <span class="social-row__dot"></span><span class="social-row__dot"></span><span class="social-row__dot"></span><span class="social-row__dot"></span>
    </div>
  </section>

  <section class="disc">
    <div class="nebula" role="img" aria-label="Teal galaxy nebula printed across the disc label"></div>
    <div class="centered" style="top:12%">
      <h2 class="album-title">HARMONUX</h2>
      <div class="album-subtitle">THE LOOP REEL</div>
    </div>
    <div class="disc__hub"></div>
    <div class="disc__hole"></div>
  </section>

</main>
</body>
</html>
```